Criação de Kit com 5 Layouts de Post para Redes Sociais (Facebook, Instagram e etc) para Consultoria de Negócios
" EVENTO DE DOIS DIAS COM VÁRIOS PALESTRANTES, TRAZENDO CONHECIMENTO EM VARIAS ÁREAS PARA AS MULHERES EMPREENDEDORAS. UM EVENTO DE IMERSSAO DE 19 HORAS. "

```html
<!DOCTYPE html>
<html lang="pt-BR">
<head>
<meta charset="UTF-8">
<title>Post – Evento de Empreendedoras</title>
<link rel="stylesheet" href="https://fonts.googleapis.com/css2?family=Cinzel:wght@400;700;900&display=swap">
<style>
  :root {
    --bg-light: #3b3b3c;
    --bg-dark: #161617;
    --gold: #c9a96a;
    --gold-light: #e8d3a2;
    --gold-deep: #9c7c45;
    --text-light: #ffffff;
    --text-dark: #1c1a17;
    --panel-edge: rgba(255,255,255,0.10);
  }
  html, body {
    margin: 0;
    padding: 0;
    overflow: hidden;
    background: var(--bg-dark);
  }
  .post {
    position: relative;
    width: 1200px;
    height: 1200px;
    overflow: hidden;
    background: radial-gradient(circle at 55% 40%, var(--bg-light) 0%, #262627 55%, var(--bg-dark) 100%);
    font-family: "Cinzel", serif;
  }
  .post__lines {
    position: absolute;
    inset: 0;
    width: 1200px;
    height: 1200px;
  }
  .post__photo {
    position: absolute;
    left: 24px;
    top: 168px;
    width: 640px;
    height: 1032px;
    border-radius: 300px 300px 0 0;
    background: linear-gradient(180deg, #5a3a2a 0%, #3a2a24 30%, #1f1f22 55%, #141416 100%);
  }
  .post__headline {
    position: absolute;
    left: 460px;
    top: 250px;
    width: 600px;
    margin: 0;
    color: var(--text-light);
    font-weight: 900;
    font-size: 37px;
    line-height: 41px;
    letter-spacing: 0.5px;
  }
  .brand {
    position: absolute;
    left: 34px;
    top: 1058px;
    display: flex;
    align-items: center;
    gap: 18px;
  }
  .brand__mark {
    width: 96px;
    height: 96px;
    border-radius: 50%;
    border: 3px solid var(--gold);
    box-sizing: border-box;
  }
  .brand__name {
    margin: 0;
    color: var(--text-light);
    font-weight: 400;
    font-size: 60px;
    line-height: 1;
    letter-spacing: 2px;
  }
  .brand__tagline {
    margin: 6px 0 0;
    color: var(--text-light);
    font-weight: 400;
    font-size: 13px;
    line-height: 16px;
    letter-spacing: 0.5px;
    width: 230px;
  }
  .site-band {
    position: absolute;
    left: 612px;
    top: 1110px;
    width: 588px;
    height: 90px;
    background: linear-gradient(90deg, var(--gold-deep) 0%, var(--gold-light) 45%, var(--gold) 75%, var(--gold-deep) 100%);
    display: flex;
    align-items: center;
    justify-content: center;
  }
  .site-band__url {
    margin: 0;
    color: var(--text-dark);
    font-weight: 700;
    font-size: 40px;
    letter-spacing: 1px;
  }
</style>
</head>
<body>
  <main class="post">
    <svg class="post__lines" viewBox="0 0 1200 1200" aria-hidden="true">
      <polygon points="648,96 1128,576 648,1056 168,576" fill="rgba(0,0,0,0.18)" stroke="var(--panel-edge)" stroke-width="3"/>
      <g stroke="var(--gold)" stroke-width="4" fill="none">
        <line x1="492" y1="0" x2="0" y2="492"/>
        <line x1="696" y1="0" x2="1200" y2="504"/>
        <line x1="1200" y1="696" x2="792" y2="1116"/>
        <line x1="0" y1="708" x2="492" y2="1200"/>
      </g>
    </svg>

    <div class="post__photo" role="img" aria-label="Foto de uma empreendedora sorridente de terno preto com os braços cruzados"></div>

    <p class="post__headline">Lorem ipsum dolor sit amet, consectetuer adi&shy;piscing elit, sed diam nonummy nibh euismod tincidunt ut laoreet dolore magna aliquam</p>

    <div class="brand">
      <div class="brand__mark"></div>
      <div class="brand__text">
        <p class="brand__name">AURA</p>
        <p class="brand__tagline">Encontro de Negócios &amp; Liderança Feminina</p>
      </div>
    </div>

    <div class="site-band">
      <p class="site-band__url">WWW.SEUEVENTO.COM.BR</p>
    </div>
  </main>
</body>
</html>
```